Flyer Tally Your Ledger Free

Hi
Can you please design me a DL Flyer for: Tally Your Ledger Free
Info:
Starting a new Business ?
Want to save on bookkeeping fees for your existing business?

You can now save 1000's off bookkeeping fees by Doing it Yourself.

Using our Bookkeeper software you simply key in the information as you go.

We offer one on one training, backup and support.
We can assist you with BAS Preparation and Payrol Advice.

Add Modules as required:
Point of Sale Module
Jobs Management Module
Website Intergration Module

Fee set up assistance and training.

Lets get the ball rolling: 1300 642 815
www.tylfr.com.au
admin@tylfr.com.au (use the logo thing you made)

Target Market(s)

Small Business

Colors
ec1f27
f04a50
f59296
fcdcdc
ffffff

Requirements
Nice to have
• image/s related to bookkeeping

```html
<!DOCTYPE html>
<html lang="en">
<head>
<meta charset="utf-8">
<title>Tally Your Ledger Free – DL Flyer</title>
<link rel="stylesheet" href="https://fonts.googleapis.com/css2?family=Montserrat:wght@400;500;700;800;900&display=swap">
<style>
  :root {
    --red: #ec1f27;
    --red-soft: #f04a50;
    --pink: #f59296;
    --blush: #fcdcdc;
    --white: #ffffff;
    --charcoal: #3b3939;
    --ink: #2a2a2a;
    --backdrop: #a7a7a7;
  }
  * { box-sizing: border-box; margin: 0; padding: 0; }
  html, body {
    width: 1200px; height: 1200px; overflow: hidden;
    background: var(--backdrop);
    font-family: "Montserrat", Arial, sans-serif;
  }
  .flyer {
    position: absolute; left: 340px; top: 48px;
    width: 520px; height: 1104px;
    background: var(--white);
    overflow: hidden;
  }
  .brand {
    position: absolute; left: 0; right: 0; top: 76px;
    text-align: center;
  }
  .brand-name {
    display: inline-flex; align-items: center; gap: 10px;
    font-weight: 800; font-size: 30px; color: var(--red);
    letter-spacing: -0.5px;
  }
  .brand-dot {
    width: 22px; height: 22px; border-radius: 50%; background: var(--red);
  }
  .hero-photo {
    position: absolute; left: 29px; top: 179px;
    width: 461px; height: 306px;
    border-top-right-radius: 76px;
    background: linear-gradient(135deg, #d9dee2 0%, #c3cbd1 40%, #b89a3a 75%, #3c4a55 100%);
  }
  .headline-band {
    position: absolute; left: 29px; top: 485px;
    width: 461px; height: 198px;
    background: linear-gradient(160deg, #f2474d 0%, #f33a40 45%, var(--red) 46%, #ff0a10 100%);
    color: var(--white); text-align: center;
  }
  .headline {
    margin-top: 20px;
    font-weight: 900; font-size: 42px; line-height: 46px; letter-spacing: 0.5px;
  }
  .headline-rule {
    width: 78px; height: 3px; background: var(--white);
    margin: 16px auto 12px;
  }
  .subhead { font-weight: 700; font-size: 18px; line-height: 22px; }
  .intro {
    position: absolute; left: 60px; right: 60px; top: 697px;
    text-align: center; font-size: 12.5px; line-height: 15px; color: var(--ink);
  }
  .intro p + p { margin-top: 5px; }
  .person-photo {
    position: absolute; left: 0; top: 757px;
    width: 172px; height: 278px;
    border-radius: 80px 80px 0 0;
    background: linear-gradient(180deg, #e8ddd6 0%, #b8c9e6 45%, #8fa8d6 75%, #222 100%);
  }
  .support-pill {
    position: absolute; left: 86px; top: 794px;
    width: 397px; height: 56px;
    background: var(--red-soft);
    border-radius: 0 28px 28px 0;
    padding: 5px 12px 0 39px;
    color: var(--white); font-size: 12px; line-height: 15.5px;
  }
  .modules {
    position: absolute; left: 237px; top: 862px; list-style: none;
    font-size: 13px; color: var(--ink);
  }
  .modules li { display: flex; align-items: center; gap: 5px; height: 26px; }
  .modules svg { width: 9px; height: 9px; }
  .setup-strip {
    position: absolute; left: 143px; top: 996px;
    width: 250px; height: 39px;
    background: var(--red);
    padding: 7px 0 0 30px;
    color: var(--white); font-weight: 900; font-size: 12px; line-height: 13px;
  }
  .contact-bar {
    position: absolute; left: 0; bottom: 0; width: 100%; height: 69px;
    background: var(--charcoal);
    color: var(--white); font-weight: 800;
    padding: 12px 0 0 43px;
  }
  .cta { font-size: 12.5px; letter-spacing: 0.2px; }
  .contact-row {
    margin-top: 11px; display: flex; align-items: center; gap: 5px; font-size: 12.5px;
  }
  .contact-row svg { width: 10px; height: 10px; }
  .contact-row .spacer { width: 4px; }
</style>
</head>
<body>
<main class="flyer">
  <header class="brand">
    <div class="brand-name"><span class="brand-dot"></span>Tally Your Ledger Free</div>
  </header>

  <div class="hero-photo" role="img" aria-label="Photo of a person in a yellow jacket using a calculator beside a laptop, glasses and printed charts"></div>

  <section class="headline-band">
    <h1 class="headline">STARTING A<br>NEW BUSINESS ?</h1>
    <div class="headline-rule"></div>
    <p class="subhead">Want to save on bookkeeping fees for<br>your existing business?</p>
  </section>

  <section class="intro">
    <p>You can now save 1000's off&nbsp; bookkeeping fees by Doing it Yourself.</p>
    <p>Using our Bookkeeper software you simply key in the information as you go.</p>
  </section>

  <div class="person-photo" role="img" aria-label="Photo of a smiling businesswoman in a blue shirt holding an open folder"></div>

  <p class="support-pill">We offer one on one training, backup and support.<br>We can assist you with BAS Preparation and<br>Payrol Advice.</p>

  <ul class="modules">
    <li><svg viewBox="0 0 10 10"><circle cx="5" cy="5" r="4.2" fill="none" stroke="#ec1f27" stroke-width="1.2"/><path d="M3 5.2l1.4 1.4L7 3.8" fill="none" stroke="#ec1f27" stroke-width="1.2"/></svg>Point of Sale Module</li>
    <li><svg viewBox="0 0 10 10"><circle cx="5" cy="5" r="4.2" fill="none" stroke="#ec1f27" stroke-width="1.2"/><path d="M3 5.2l1.4 1.4L7 3.8" fill="none" stroke="#ec1f27" stroke-width="1.2"/></svg>Jobs Management Module</li>
    <li><svg viewBox="0 0 10 10"><circle cx="5" cy="5" r="4.2" fill="none" stroke="#ec1f27" stroke-width="1.2"/><path d="M3 5.2l1.4 1.4L7 3.8" fill="none" stroke="#ec1f27" stroke-width="1.2"/></svg>Website Intergration Module</li>
  </ul>

  <p class="setup-strip">Fee set up assistance<br>and training.</p>

  <footer class="contact-bar">
    <p class="cta">LETS GET THE BALL ROLLING: 1300 642 815</p>
    <p class="contact-row">
      <svg viewBox="0 0 10 10"><circle cx="5" cy="5" r="4.5" fill="#ec1f27"/><path d="M0.5 5h9M5 0.5c-2.4 2.6-2.4 6.4 0 9M5 0.5c2.4 2.6 2.4 6.4 0 9" fill="none" stroke="#3b3939" stroke-width="0.7"/></svg>
      www.tylfr.com.au
      <span class="spacer"></span>
      <svg viewBox="0 0 10 10"><rect x="0.5" y="2" width="9" height="6.5" fill="#ec1f27"/><path d="M0.5 2l4.5 3.5L9.5 2" fill="none" stroke="#3b3939" stroke-width="0.8"/></svg>
      admin@tylfr.com.au
    </p>
  </footer>
</main>
</body>
</html>
```